Hadley & Partners, LLC Business Card 2016

We need a new business card design for a very important trade show coming up.

We are a compliance Consulting Firm. Our clients are stock brokerage firms and investment advisers.

I would like our logo on both sides of the card.

Info in the front of the card shold include:

Logo
First & Last Name
Title
Office #
Cell #
Email
Company Address (42 W. Calloway St., Suite 300 Pasadena, CA 91417

Back of the card should include the logo and url: www.hadleypartnersgroup.com

Target Market(s)

Stock Brokerage Firms and Investment Advisers

Industry/Entity Type

Financial Service

Contact Information for Business Card

Marcus J. Pellew
President
42 W. Calloway St., Suite 300
Pasadena, CA 91417
O 626.555.0147 ext. 204
C 818.555.0193
Email: marcus@hadleypartnersgroup.com
www.hadleypartnersgroup.com

Requirements
Nice to have
• The back of the card could be black with the logo with the white letters.
• I do want the front of the card to at least have the color logo with the black "Hadley & Partners Lettering.

```html
<!DOCTYPE html>
<html lang="en">
<head>
<meta charset="utf-8">
<title>Hadley &amp; Partners — Business Card</title>
<link href="https://fonts.googleapis.com/css2?family=Montserrat:wght@600;700&display=swap" rel="stylesheet">
<style>
  :root {
    --page: #ffffff;
    --card-light: #e6e7e9;
    --panel-grey: #848b93;
    --ink-black: #1b1b1b;
    --card-dark: #2b2b2b;
    --brand-red: #c8201c;
    --brand-ink: #2a2a2a;
    --white: #ffffff;
  }
  * { margin: 0; padding: 0; box-sizing: border-box; }
  html, body {
    width: 975px; height: 1200px; overflow: hidden;
    background: var(--page);
    font-family: "Montserrat", Arial, sans-serif;
  }
  .card {
    position: absolute; left: 50px; width: 872px; height: 499px;
    border-radius: 28px; overflow: hidden;
  }
  .card-front { top: 64px; background: var(--card-light); }
  .card-back { top: 605px; background: var(--card-dark); }

  .front-shapes { position: absolute; inset: 0; }

  .brand { position: absolute; text-align: center; }
  .brand-square { display: block; margin: 0 auto 34px; width: 96px; height: 96px; background: var(--brand-red); }
  .brand-name {
    font-weight: 700; font-size: 40px; line-height: 1.15; letter-spacing: 2px;
  }
  .card-front .brand { left: 24px; width: 380px; top: 100px; }
  .card-front .brand-name { color: var(--brand-ink); }
  .card-back .brand { left: 0; width: 872px; top: 92px; }
  .card-back .brand-name { color: var(--white); }

  .person {
    position: absolute; left: 480px; width: 320px; top: 40px;
    text-align: center; color: var(--white);
  }
  .person-name { font-weight: 700; font-size: 30px; }
  .person-title { font-weight: 700; font-size: 21px; margin-top: 18px; letter-spacing: 0.5px; }

  .contact { position: absolute; left: 486px; color: var(--white); font-weight: 700; font-size: 19px; line-height: 34px; }
  .contact-phones { top: 200px; }
  .contact-phones span { display: inline-block; width: 92px; }
  .contact-email { top: 284px; }
  .contact-web { top: 342px; }
  .contact-address { top: 398px; line-height: 25px; }

  .icon { position: absolute; left: 424px; width: 32px; height: 32px; }

  .back-url {
    position: absolute; left: 0; width: 872px; top: 456px;
    text-align: center; color: var(--white); font-weight: 700; font-size: 22px;
  }
  .back-rules { position: absolute; left: 0; top: 0; }
</style>
</head>
<body>

<section class="card card-front">
  <svg class="front-shapes" width="872" height="499" viewBox="0 0 872 499">
    <path d="M407 0 H872 V499 H440 C440 460 407 420 407 380 Z" fill="var(--ink-black)"/>
    <path d="M415 0 H872 V499 H479 C479 470 444 450 444 420 V210 C444 180 415 160 415 120 Z" fill="var(--panel-grey)"/>
  </svg>

  <div class="brand">
    <span class="brand-square"></span>
    <div class="brand-name">HADLEY<br>&amp; PARTNERS</div>
  </div>

  <div class="person">
    <div class="person-name">Marcus J. Pellew</div>
    <div class="person-title">PRESIDENT</div>
  </div>

  <svg class="icon" style="top:216px" viewBox="0 0 32 32" fill="none" stroke="var(--white)" stroke-width="1.8" stroke-linejoin="round">
    <path d="M8 4 L12 4 L14 11 L11 13 C12 17 15 20 19 21 L21 18 L28 20 L28 24 C28 27 25 28 22 27 C13 25 7 19 5 10 C4 7 5 4 8 4 Z"/>
    <path d="M19 6 C23 7 25 9 26 13 M19 10 C21 11 22 12 22 14"/>
  </svg>
  <svg class="icon" style="top:286px" viewBox="0 0 32 32">
    <rect x="3" y="7" width="26" height="18" fill="var(--white)"/>
    <path d="M3 7 L16 18 L29 7 M3 25 L12 15 M29 25 L20 15" fill="none" stroke="var(--ink-black)" stroke-width="1.6"/>
  </svg>
  <svg class="icon" style="top:342px" viewBox="0 0 32 32" fill="none" stroke="var(--white)" stroke-width="1.5">
    <circle cx="16" cy="16" r="12"/>
    <ellipse cx="16" cy="16" rx="5.5" ry="12"/>
    <path d="M4 16 H28 M6 10 H26 M6 22 H26"/>
  </svg>
  <svg class="icon" style="top:398px" viewBox="0 0 32 32" fill="var(--white)">
    <path d="M16 4 L30 16 L27 16 L27 29 L5 29 L5 16 L2 16 Z"/>
    <rect x="13" y="19" width="6" height="10" fill="var(--ink-black)"/>
    <rect x="22" y="5" width="3" height="7"/>
  </svg>

  <div class="contact contact-phones">
    <div><span>(Office)</span>: 626 555 0147 (204)</div>
    <div><span>(Cell)</span>: 818 555 0193</div>
  </div>
  <div class="contact contact-email">marcus@hadleypartnersgroup.com</div>
  <div class="contact contact-web">www.hadleypartnersgroup.com</div>
  <div class="contact contact-address">42 W. Calloway St., Suite 300<br>Pasadena, CA 91417</div>
</section>

<section class="card card-back">
  <div class="brand">
    <span class="brand-square"></span>
    <div class="brand-name">HADLEY<br>&amp; PARTNERS</div>
  </div>
  <svg class="back-rules" width="872" height="499" viewBox="0 0 872 499">
    <polygon points="17,472 208,466 208,471" fill="var(--white)"/>
    <polygon points="658,466 850,472 658,471" fill="var(--white)"/>
  </svg>
  <div class="back-url">www.hadleypartnersgroup.com</div>
</section>

</body>
</html>
```